Harvest Gate Fellowship Network needs a fresh new web design

We are an up and coming multicultural church that aims to bring people into a life changing encounter with God. We need a fresh and inviting website in order to increase our internet presence and make us easier to connect with.
Here are some of the basic requirements for the site:
• Clearly displayed address, service times, and contact info
• A staff profile page
• An area for a calendar with upcoming events and their details
• Social media buttons
• Group pages for the different ministries (youth, children’s church, men, etc…)
• An area for donations and eCommerce
• A resources page for assorted media (podcasts, sermons, videos, etc.…)
• An area for prayer requests.

Industry/Entity Type

Church

```html
<!DOCTYPE html>
<html lang="en">
<head>
<meta charset="utf-8">
<title>Harvest Gate Fellowship Network</title>
<link rel="stylesheet" href="https://fonts.googleapis.com/css2?family=Source+Sans+3:ital,wght@0,400;0,600;1,400;1,600&display=swap">
<style>
:root{
  --navy:#0d2a6e;
  --navy-dark:#0a1f57;
  --cream:#fefde6;
  --header-top:#f6f3e1;
  --header-bottom:#ece6c8;
  --nav-bg:#ebe5c6;
  --rule:#d8d0a8;
  --ink:#333;
  --muted:#858585;
  --heading:#4a4a4a;
  --gold:#e7be45;
  --gold-light:#f6d977;
  --footer:#dbc47b;
  --footer-text:#7a6322;
  --footer-bottom:#c6a138;
}
*{box-sizing:border-box;margin:0;padding:0}
html,body{width:799px;height:1200px;overflow:hidden}
body{background:var(--cream);font-family:"Source Sans 3",sans-serif;font-weight:400;color:var(--ink);position:relative}
.abs{position:absolute}
.topbar{left:0;top:0;width:799px;height:6px;background:var(--navy-dark)}
.header{left:0;top:6px;width:799px;height:102px;background:linear-gradient(var(--header-top),var(--header-bottom))}
.brand{left:80px;top:36px;display:flex;align-items:center;gap:10px}
.brand-mark{width:58px;height:58px;border-radius:50%;background:var(--gold-light);flex:none}
.brand-name{font-size:18px;color:var(--navy);font-weight:400;letter-spacing:.1px}
.contact{right:81px;top:32px;text-align:right;font-size:8.5px;line-height:15px;color:#555;font-weight:400}
.contact .phone{font-size:14px;color:#444;line-height:22px}
.nav{left:0;top:108px;width:799px;height:26px;background:var(--nav-bg);border-top:1px solid var(--rule);border-bottom:1px solid var(--rule)}
.nav ul{list-style:none;display:flex;position:absolute;left:81px;top:7px;font-size:8px;color:#222}
.nav li{padding:0 9px;border-left:1px solid #cfc6a0;line-height:10px}
.nav li:first-child{padding-left:0;border-left:none}
.nav li.sep{border-left:1px solid #333}
.hero{left:80px;top:146px;width:639px;height:250px;background:linear-gradient(100deg,#cfcfcc 0%,#b9b9b4 45%,#6f6a72 70%,#2e3550 100%)}
.caption{left:448px;top:334px;width:254px;height:48px;background:#fff;font-style:italic;font-size:12px;color:#222;display:flex;align-items:center;padding-left:18px}
.dots{left:702px;top:334px;width:16px;height:48px;background:var(--navy);display:flex;flex-direction:column;align-items:center;justify-content:center;gap:4px}
.dots span{width:7px;height:7px;border-radius:50%;background:#e6d88a}
h2{font-weight:400;font-size:14px;color:var(--heading)}
.body{font-size:7.5px;line-height:15px;color:var(--muted);font-weight:400}
.btn{display:inline-block;background:var(--navy);color:#fff;font-size:7.5px;font-style:italic;padding:0 6px;height:19px;line-height:19px}
.photo{background:linear-gradient(135deg,#b7a898,#6b5a4f)}
.donate{left:565px;top:450px;width:154px;height:52px;background:#fff;border:1px solid #c9c9c9;padding:3px 7px}
.donate .lead{font-size:13px;color:var(--navy)}
.donate .row{display:flex;align-items:center;gap:6px;margin-top:2px}
.donate .pay{font-size:16px;font-weight:600;color:var(--navy)}
.donate .card{width:16px;height:10px;background:#c9c9c9}
.prayer{left:565px;top:522px;width:154px;height:52px;background:linear-gradient(90deg,var(--gold),var(--gold-light));color:#fff;font-size:13px;line-height:18px;padding:5px 7px}
.prayer .hands{position:absolute;right:0;top:0;width:48px;height:52px;background:linear-gradient(90deg,#e9d9c6,#c9b29a)}
.ministry h3{font-weight:400;font-size:10px;color:#444;margin-top:8px}
.ministry .body{margin-top:2px}
.ministry .btn{margin-top:9px}
.video{left:78px;top:868px;width:233px;height:195px;background:linear-gradient(135deg,#f1dd8c,#e3b845 60%,#8a7a5a)}
.video .bar{position:absolute;left:0;right:0;height:12px;background:#1e1e1e}
.play{left:98px;top:82px;width:30px;height:30px;background:#111;border-radius:3px}
.event{left:342px;width:378px}
.event .date{position:absolute;left:0;top:0;width:42px;height:42px}
.event .date span{position:absolute;left:0;right:0;top:20px;text-align:center;font-size:7.5px;font-weight:600;color:#555}
.event .body{position:absolute;left:50px;top:0}
.event .more{color:var(--navy);font-size:8px;font-weight:400;display:block;padding-left:2px}
.footer{left:0;top:1116px;width:799px;height:50px;background:var(--footer)}
.footer nav{position:absolute;left:80px;top:19px;font-size:9px;color:var(--footer-text)}
.social{position:absolute;left:437px;top:14px;display:flex;gap:18.5px}
.social span{width:19px;height:19px;border-radius:50%;background:#f7f0d7;border:1px solid #c7b06a}
.copy{left:0;top:1166px;width:799px;height:34px;background:var(--footer-bottom);font-size:8px;color:#fff;padding:11px 0 0 79px}
</style>
</head>
<body>
<div class="abs topbar"></div>
<header class="abs header"></header>
<div class="abs brand"><span class="brand-mark"></span><span class="brand-name">Harvest Gate Fellowship Network</span></div>
<div class="abs contact">
  <div>482 W Meadowlark Ave Ste 12 , Riverton OR 97410</div>
  <div>Email: info@harvestgatefellowship.org</div>
  <div>Hours: Mon-Fri: 7am - 6pm</div>
  <div class="phone">+ 555.013.2746</div>
</div>
<nav class="abs nav"><ul>
  <li>HOME</li><li>ABOUT US</li><li>EVENTS</li><li>PRAYER REQUEST</li><li>DONATE</li><li class="sep">CONTACT US</li>
</ul></nav>

<div class="abs hero" role="img" aria-label="Smiling couple in a bright church hall with rows of chairs and a keyboard"></div>
<div class="abs caption">WE HOPE YOU WILL VISIT US REAL SOON</div>
<div class="abs dots"><span></span><span></span><span></span></div>

<section class="abs" style="left:80px;top:417px;width:210px">
  <h2>Welcome to HGFN</h2>
  <p class="body" style="margin-top:15px">Aenean sollicitudin, lorem quis bibendum auctor, nisi elit consequat ipsum, nec sagittis sem nibh id elit. Duis sed dio sit amet nibh vulputate cursus a sit amet mauris.</p>
  <p class="body" style="margin-top:15px">Morbicumsan ipsum velit. Nam nec tellus a odio tincidunt auctor a ornare odio. Sed non &nbsp;mauris vitae erat consequat auctor eu in elit. Class aptent taciti sociosqu ad litora</p>
  <span class="btn" style="margin-top:11px">READ MORE</span>
</section>

<h2 class="abs" style="left:312px;top:417px">Staff Profile</h2>
<div class="abs photo" style="left:311px;top:450px;width:100px;height:140px" role="img" aria-label="Group portrait of the church staff"></div>
<div class="abs" style="left:417px;top:450px;width:135px">
  <p class="body">Aenean sollicitudin, lorem quis bibendum auctor, nisi elit consequat ipsum, nec sagittis sem nibh id elit.</p>
  <p class="body" style="margin-top:15px">Duis sed dio sit amet nibh vulputate cursus a sit amet mauris. orbicumsan ipsum velitam nec.</p>
  <span class="btn" style="margin-top:11px;margin-left:2px">READ MORE</span>
</div>

<div class="abs donate">
  <div class="lead">Donate now with</div>
  <div class="row"><span class="pay">Kindrell Pay</span><span class="card"></span><span class="card"></span></div>
</div>
<div class="abs prayer">Submit<br>Prayer Request<span class="hands" role="img" aria-label="Hands folded in prayer"></span></div>

<h2 class="abs" style="left:79px;top:613px">Ministries</h2>
<article class="abs ministry" style="left:79px;top:645px;width:203px">
  <div class="photo" style="height:87px;background:linear-gradient(135deg,#6a4a3a,#e9d2c0 60%,#9aa0a0)" role="img" aria-label="Family reading the Bible together"></div>
  <h3>Mauris in erat justo</h3>
  <p class="body">Aenean sollicitudin, lorem quis bibendum auctor, nisi elit consequat ipsum, nec sagittis sem nibh id elit. Duis sed dio sit amet nibh vulputate cursus a sit amet</p>
  <span class="btn">READ MORE</span>
</article>
<article class="abs ministry" style="left:298px;top:645px;width:203px">
  <div class="photo" style="height:87px;background:linear-gradient(135deg,#c8a67a,#e7d9c8 50%,#b48552)" role="img" aria-label="Children seated on church pews"></div>
  <h3>Mauris in erat justo</h3>
  <p class="body">Aenean sollicitudin, lorem quis bibendum auctor, nisi elit consequat ipsum, nec sagittis sem nibh id elit. Duis sed dio sit amet nibh vulputate cursus a sit amet</p>
  <span class="btn" style="margin-left:2px">READ MORE</span>
</article>
<article class="abs ministry" style="left:516px;top:645px;width:203px">
  <div class="photo" style="height:87px;background:linear-gradient(135deg,#d9cfc0,#a08770 50%,#c9b9a5)" role="img" aria-label="Minister standing in a sanctuary with a stained glass window"></div>
  <h3>Mauris in erat justo</h3>
  <p class="body">Aenean sollicitudin, lorem quis bibendum auctor, nisi elit consequat ipsum, nec sagittis sem nibh id elit. Duis sed dio sit amet nibh vulputate cursus a sit amet</p>
  <span class="btn" style="margin-left:3px">READ MORE</span>
</article>

<div class="abs video" role="img" aria-label="Video player showing a women's conference flyer">
  <div class="bar" style="top:0"></div>
  <div class="bar" style="bottom:0"></div>
  <div class="abs play"><svg width="30" height="30" viewBox="0 0 30 30"><path d="M12 9 L21 15 L12 21 Z" fill="#fff"/></svg></div>
</div>

<h2 class="abs" style="left:342px;top:867px">Upcoming Events</h2>
<svg width="0" height="0" style="position:absolute"><defs>
  <symbol id="cal" viewBox="0 0 42 42"><rect x="1.5" y="5" width="39" height="35" rx="5" fill="#fff" stroke="#d6b35a" stroke-width="3"/><rect x="1.5" y="5" width="39" height="8" fill="#d6b35a"/><rect x="10" y="1" width="4" height="9" rx="2" fill="#d6b35a"/><rect x="28" y="1" width="4" height="9" rx="2" fill="#d6b35a"/></symbol>
</defs></svg>
<div class="abs event" style="top:894px">
  <div class="date"><svg width="42" height="42"><use href="#cal"/></svg><span>20 June</span></div>
  <div class="body">Aenean sollicitudin, lorem quis bibendum auctor, nisi elit consequat ipsum, auctor eu in elit.<br>Class aptent taciti sociosqu ad litora torquent per conubia nostra.<span class="more">Read More</span></div>
</div>
<div class="abs event" style="top:958px">
  <div class="date"><svg width="42" height="42"><use href="#cal"/></svg><span>27 June</span></div>
  <div class="body">Aenean sollicitudin, lorem quis bibendum auctor, nisi elit consequat ipsum, auctor eu in elit.<br>Class aptent taciti sociosqu ad litora torquent per conubia nostra.<span class="more">Read More</span></div>
</div>
<div class="abs event" style="top:1020px">
  <div class="date"><svg width="42" height="42"><use href="#cal"/></svg><span>30 June</span></div>
  <div class="body">Aenean sollicitudin, lorem quis bibendum auctor, nisi elit consequat ipsum, auctor eu in elit.<br>Class aptent taciti sociosqu ad litora torquent per conubia nostra.<span class="more">Read More</span></div>
</div>

<footer class="abs footer">
  <nav>Home &nbsp;|&nbsp; About Us &nbsp;|&nbsp; Events &nbsp;|&nbsp; Prayer Request &nbsp;|&nbsp; Donate &nbsp;|&nbsp; Contact Us</nav>
  <div class="social"><span></span><span></span><span></span><span></span><span></span><span></span><span></span><span></span></div>
</footer>
<div class="abs copy">© 2014 HGFN. All Rights Reserved &nbsp;|&nbsp; Privacy Policy &nbsp;|&nbsp; Terms Conditions</div>
</body>
</html>
```